Brochure for teeth whitening business

I require a double-sided card type brochure for my teeth whitening business. The information on want on it is:
Qualified personnel
Members of the Pacific Brightline Smile Care Guild (PBSCG)
We offer teeth whitening treatments using state of the art equipment in a relaxed environment.
Before and after photos (I still need to attach these for the brochure)
PRICE LIST
Full treatment - first time (1hr 20 incls consult): $300
Full treatment (1hr): $275
Touch-up treatment
1 x 20 minute: $100
2 x 20 minute: $180
ZERO Peroxide full treatment - first time (1hr 20 incls consult): $400
ZERO Peroxide full treatment (1hr)
Touch-up treatment - ZERO Peroxide
1 x 20 minute: $150
2 x 20 minute: $280
Take home whitening pen: $45
(can be purchased in-clinic or from our website)
Discounts apply for weddings, corporates, and couples. Please see our website for more details.
We have a clinic in Hawera and Opunake and also offer a mobile service where we can come to you.
We understand life can be hectic hence we are flexible with our opening hours with appointments available 7 days a week.
Call us today for an appointment or alternatively visit our website to conveniently book your own appointment at a time that suits you!
Contact number: 022 918 6403
Email: glowpearldental@mailbox-demo.net
Website: www.glowpearlbooking.example
NOTE: Please add your marketing/advertising touches to the brochure, I am happy for you to add words to market/advertise and attract people to want to book in to get their teeth whitened.
People who have stained teeth, smokers, green tea/coffee drinkers etc will greatly benefit from teeth whitening.
Updates
Hi, please note the few minor changes to my brief. Have just added a couple of things. Thank you
Target Market(s)
Target customers are wedding parties, hens parties, glamour photo, older people with stained teeth, also younger people (20's and up)
Industry/Entity Type
Clinic
Look and feel
Each slider illustrates characteristics of the customer's brand and the style your logo design should communicate.

```html
<!DOCTYPE html>
<html lang="en">
<head>
<meta charset="utf-8">
<title>Teeth Whitening Brochure</title>
<link rel="stylesheet" href="https://fonts.googleapis.com/css2?family=Questrial&display=swap">
<style>
  :root {
    --brand-blue: #1d72a1;
    --panel-blue: #226e94;
    --panel-heading: #9ad8f2;
    --panel-note: #7cbde0;
    --ink: #1a1a1a;
    --paper: #ffffff;
  }
  html, body { margin: 0; padding: 0; overflow: hidden; background: var(--paper); }
  .brochure {
    position: relative;
    width: 1200px;
    height: 928px;
    overflow: hidden;
    background: var(--paper);
    font-family: "Questrial", "Century Gothic", sans-serif;
    color: var(--ink);
  }
  .brochure p, .brochure h1, .brochure h2, .brochure ul { margin: 0; }
  .photo-strip { position: absolute; left: 0; top: 0; }

  /* Left column: contact */
  .contact > * { position: absolute; left: 26px; white-space: nowrap; }
  .contact .cta { top: 434px; color: var(--brand-blue); font-weight: 700; font-size: 61px; line-height: 64px; letter-spacing: -1.5px; }
  .contact .cta-sub { top: 488px; color: var(--brand-blue); font-size: 35px; line-height: 40px; }
  .contact .label { font-size: 34px; line-height: 40px; }
  .contact .label-phone { top: 544px; }
  .contact .label-email { top: 637px; }
  .contact .phone { top: 587px; color: var(--brand-blue); font-size: 46px; line-height: 50px; }
  .contact .email { top: 675px; color: var(--brand-blue); font-size: 21px; line-height: 28px; }
  .contact .or { top: 743px; color: var(--brand-blue); font-size: 35px; line-height: 40px; }
  .contact .web-note { top: 780px; width: 355px; white-space: normal; font-size: 21px; line-height: 25.5px; }

  /* Middle column: packages */
  .packages-panel {
    position: absolute;
    left: 401px; top: 346px;
    width: 399px; height: 582px;
    background: var(--panel-blue);
    color: var(--paper);
  }
  .packages-panel .section { position: absolute; left: 29px; width: 342px; }
  .packages-panel .wedding { top: 12px; }
  .packages-panel .corporate { top: 226px; }
  .packages-panel .couples { top: 418px; }
  .packages-panel h2 { margin-bottom: 8px; font-weight: 400; font-size: 22px; line-height: 28px; color: var(--panel-heading); }
  .packages-panel p { margin-bottom: 13px; font-size: 13px; line-height: 17px; }
  .packages-panel ul { list-style: none; padding: 0; font-size: 14.5px; line-height: 18px; }
  .packages-panel .fine-print { margin-top: 16px; color: var(--panel-note); font-size: 10.5px; line-height: 13.5px; }

  /* Right column: price list */
  .price-row { position: absolute; left: 817px; width: 366px; display: flex; justify-content: space-between; align-items: flex-start; }
  .price-row .item { font-size: 24px; line-height: 28px; }
  .price-row .item small { display: block; font-size: 18px; line-height: 20px; }
  .price-row .item .inline-note { font-size: 18px; }
  .price-row .price { color: var(--brand-blue); font-size: 33px; line-height: 38px; }
  .row-first { top: 400px; }
  .row-full { top: 483px; }
  .row-touch { top: 544px; }
  .row-touch-1 { top: 570px; }
  .row-touch-2 { top: 595px; }
  .sub-row { padding-left: 20px; box-sizing: border-box; }
  .sub-row .item { font-size: 21px; line-height: 25px; }
  .sub-row .price { font-size: 28px; line-height: 25px; }
  .row-zero { top: 652px; }
  .row-pen { top: 733px; }

  .discounts { position: absolute; left: 800px; top: 796px; width: 400px; text-align: center; }
  .discounts .lead { font-size: 19.5px; line-height: 26px; }
  .discounts .cta { color: var(--brand-blue); font-size: 27px; line-height: 32px; margin-bottom: 6px; }
  .discounts .small { font-size: 15px; line-height: 18px; }
  .discounts .web { color: var(--brand-blue); }
</style>
</head>
<body>
<div class="brochure">

  <svg class="photo-strip" width="1200" height="400" viewBox="0 0 1200 400">
    <defs>
      <linearGradient id="couple-young" x1="0" y1="0" x2="1" y2="1">
        <stop offset="0" stop-color="#e8e4df"/>
        <stop offset="0.5" stop-color="#d9b39a"/>
        <stop offset="1" stop-color="#f4f1ee"/>
      </linearGradient>
      <linearGradient id="couple-older" x1="0" y1="0" x2="1" y2="1">
        <stop offset="0" stop-color="#e9e7e4"/>
        <stop offset="0.55" stop-color="#d6a98f"/>
        <stop offset="1" stop-color="#3a3a42"/>
      </linearGradient>
      <linearGradient id="single-smile" x1="0" y1="0" x2="1" y2="1">
        <stop offset="0" stop-color="#e9d2a8"/>
        <stop offset="0.6" stop-color="#ecc8b4"/>
        <stop offset="1" stop-color="#f6f0ec"/>
      </linearGradient>
    </defs>
    <g role="img" aria-label="Photo of a smiling young couple">
      <rect x="380" y="0" width="450" height="346" fill="url(#couple-young)"/>
    </g>
    <g role="img" aria-label="Photo of a smiling older couple">
      <path d="M0 0 H410 V299 A325 325 0 0 1 0 323 Z" fill="url(#couple-older)" stroke="#ffffff" stroke-width="6"/>
    </g>
    <g role="img" aria-label="Photo of a laughing woman with white teeth">
      <path d="M790 0 H1200 V339 A360 360 0 0 1 790 290 Z" fill="url(#single-smile)" stroke="#ffffff" stroke-width="6"/>
    </g>
  </svg>

  <section class="contact">
    <h1 class="cta">call us today</h1>
    <p class="cta-sub">for an appointment</p>
    <p class="label label-phone">Contact number:</p>
    <p class="phone">022 918 6403</p>
    <p class="label label-email">Email:</p>
    <p class="email">glowpearldental@mailbox-demo.net</p>
    <p class="or">Or...</p>
    <p class="web-note">You may visit our website, where you can conveniently book your own appointment at a time that's suitable for you!</p>
  </section>

  <section class="packages-panel">
    <div class="section wedding">
      <h2>Wedding packages</h2>
      <p>Whiten your smile for your big day and have your smile stand out in your photos! Treat yourselves (you and your fiancé) and include your bridal party for a special price by booking one of our packages below:</p>
      <ul>
        <li>Bride &amp; Groom: $500</li>
        <li>Bride &amp; Groom + 2: $800</li>
        <li>Bride &amp; Groom + 4: $1200</li>
        <li>Bride &amp; Groom + 6: $1440</li>
      </ul>
    </div>
    <div class="section corporate">
      <h2>Corporate packages</h2>
      <p>Treat your employees to a glowpearl smile with our special deals for corporates. With our mobile service, we can come to your workplace.</p>
      <ul>
        <li>1 – 3 persons: $250 per person</li>
        <li>4 – 6 persons: $200 per person</li>
        <li>7 – 9 persons: $180 per person</li>
        <li>10+ persons: $160 per person</li>
      </ul>
    </div>
    <div class="section couples">
      <h2>Couples package</h2>
      <p>We offer a couples package so bring along your partner, friend, or relative! Special price of $250 per person (SAVE $25 per person).</p>
      <p class="fine-print">Please note: These package deals are for a first time full treatment and DO NOT include ZERO peroxide treatments. For a special deal on this treatment, please contact us by email.</p>
    </div>
  </section>

  <section class="price-list">
    <div class="price-row row-first">
      <div class="item">First time full treatment<small>(incl consult)</small></div>
      <div class="price">$300</div>
    </div>
    <div class="price-row row-full">
      <div class="item">Full treatment <span class="inline-note">(1hr)</span></div>
      <div class="price">$275</div>
    </div>
    <div class="price-row row-touch">
      <div class="item">Touch-up treatments</div>
    </div>
    <div class="price-row sub-row row-touch-1">
      <div class="item">1 x 20 minutes</div>
      <div class="price">$100</div>
    </div>
    <div class="price-row sub-row row-touch-2">
      <div class="item">2 x 20 minutes</div>
      <div class="price">$180</div>
    </div>
    <div class="price-row row-zero">
      <div class="item">ZERO Peroxide treatment<small>(1hr)</small></div>
      <div class="price">$400</div>
    </div>
    <div class="price-row row-pen">
      <div class="item">Take home whitening pen</div>
      <div class="price">$45</div>
    </div>
  </section>

  <section class="discounts">
    <p class="lead">Discounts apply for groups and couples.</p>
    <p class="cta">phone or email us for details.</p>
    <p class="small">For wedding, corporate, and couples deals,<br>please visit us at: <span class="web">www.glowpearlbooking.example</span></p>
  </section>

</div>
</body>
</html>
```